Veltrix Stationary

Design the stationary of Veltrix Promotions Group.

Veltrix is a BTL company, BTL meaning "below the line". In other words Veltrix is a Promotional Marketing company (the company that design the brands promotional activities).

The design should transmit creativity, agility, boldness.

I need:
* Bis Card
* Letter head
* Envelopes, both vertical and horizontal (for legal size), and letter envelope
* Folders
* PPT template (Title page and regular page)
* CD slip (CD envelope)
* ID card (employee card)

And what ever else you want to throw in.
Updates

Guys,

Something I missed from the brief.   The predominat color should be RED.

Also, have fun and play with the exclamation mark (!) of the logo. 

Hi guys, more comments:

Remember that Veltrix is a "creativity" agency, not in the advertising side but on the promotional side, and that should reflect on the stationary.

 I want a bold design.  Bold and yet crisp.

 

Guys, i just uploaded the Logo in AI format.

I Also uploaded the actual Veltrix Bis Card, wich I like.  So I will like to see some designs with that bis card approach.

Guys, I am so sorry, but I notice in your last post that I upladed a wrong design ("13154_marketing_group_veltrix_brief225630.ai").  The problem was that I asked the designer the file in AI format and he send me thw wrong file, and since I dont have Illustrator I could not verify it.

The differences are minor, I just already ask him the correct one (similar to the EPS file).

Sorry                                   

Just post the correct AI file : "Veltrix Logo.ai"

Reason: I'm expecting more designs to choose from and also I wont be available tomorrow to decide.

Reason: Sorry guys, but we are not there yet!

Target Market(s)

Marketing directors, Marketing Managers

Industry/Entity Type

Legal

Requirements
Must have
• Must work with the logo attached.
The predominat color should be RED.
Play and have fun with the exclamation mark (!).
Should not have
• * No old fonts

Should not be:
* boring
* Informal
* rigid

```html
<!DOCTYPE html>
<html lang="en">
<head>
<meta charset="utf-8">
<title>Veltrix Promotions Group – Stationery</title>
<link rel="stylesheet" href="https://fonts.googleapis.com/css2?family=Montserrat:wght@800&family=Open+Sans:wght@400&family=Della+Respira&family=Josefin+Sans:ital,wght@1,300&display=swap">
<style>
  :root {
    --brand-red: #d0171f;
    --paper: #f2f2f3;
    --ink: #1c1c1c;
    --muted: #6e6e70;
    --rule: #c9c9cc;
    --white: #ffffff;
  }
  * { margin: 0; padding: 0; box-sizing: border-box; }
  html, body { width: 1200px; height: 1045px; overflow: hidden; background: var(--white); }
  .canvas { position: relative; width: 1200px; height: 1045px; }

  .wordmark {
    position: absolute;
    display: flex;
    align-items: center;
    font-family: "Montserrat", sans-serif;
    font-weight: 800;
    color: var(--ink);
    letter-spacing: -0.5px;
    line-height: 1;
  }
  .wordmark-dot { border-radius: 50%; background: var(--brand-red); flex: none; }

  /* Letterhead */
  .letterhead { position: absolute; left: 388px; top: 108px; width: 612px; height: 792px; }
  .letterhead svg { position: absolute; inset: 0; }
  .letterhead .wordmark { left: 380px; top: 42px; font-size: 40px; gap: 10px; }
  .letterhead .wordmark-dot { width: 22px; height: 22px; }
  .cd-wordmark { left: 253px !important; top: 456px !important; font-size: 22px !important; gap: 6px !important; }
  .cd-wordmark .wordmark-dot { width: 12px !important; height: 12px !important; }

  .contact {
    font-family: "Josefin Sans", sans-serif;
    font-style: italic;
    font-weight: 300;
    font-variant: small-caps;
    color: var(--muted);
    letter-spacing: 1.8px;
  }
  .letter-footer {
    position: absolute; left: 35px; top: 710px; width: 520px;
    border-top: 1.5px dashed var(--rule);
    padding-top: 6px;
    font-size: 11px; line-height: 13.2px;
  }

  /* Business card front */
  .card-front {
    position: absolute; left: 117px; top: 399px; width: 251px; height: 144px;
    background: var(--paper); border-radius: 8px;
  }
  .card-front .wordmark { left: 168px; top: 16px; font-size: 17px; gap: 5px; }
  .card-front .wordmark-dot { width: 10px; height: 10px; }
  .name-tab {
    position: absolute; left: 0; top: 38px; width: 155px; height: 53px;
    background: var(--brand-red); border-radius: 0 8px 8px 0;
    text-align: right; padding: 14px 10px 0 0; color: var(--white);
    font-family: "Della Respira", serif;
  }
  .name-tab .person-name { font-size: 15px; line-height: 16px; }
  .name-tab .person-role { font-size: 9px; line-height: 12px; }
  .card-contact {
    position: absolute; right: 13px; top: 97px; text-align: right;
    font-size: 7.5px; line-height: 9.3px; letter-spacing: 1.3px;
  }

  /* Business card back */
  .card-back {
    position: absolute; left: 113px; top: 564px; width: 253px; height: 144px;
    background: var(--brand-red); border-radius: 6px;
    color: var(--white); font-family: "Open Sans", sans-serif; text-align: center;
  }
  .card-back .tagline { position: absolute; left: 0; right: 0; top: 57px; font-size: 19.5px; line-height: 24px; padding-left: 16px; }
  .card-back .url { position: absolute; left: 0; right: 0; top: 82px; font-size: 7.5px; padding-left: 16px; }
</style>
</head>
<body>
<main class="canvas">

  <section class="letterhead" aria-label="Letterhead with CD">
    <svg width="612" height="792" viewBox="0 0 612 792">
      <rect class="sheet" width="612" height="792" fill="var(--paper)"/>
      <path class="sweep-top" d="M0 0 H612 V4 C380 14 90 70 0 190 Z" fill="var(--brand-red)"/>
      <path class="sweep-bottom" d="M612 677 C604 750 540 786 440 792 H612 Z" fill="var(--brand-red)"/>
      <g class="cd-disc">
        <circle cx="204" cy="466" r="170" fill="var(--paper)" stroke="var(--brand-red)" stroke-width="4"/>
        <rect x="38" y="448" width="130" height="58" fill="var(--brand-red)"/>
        <circle cx="204" cy="466" r="51" fill="var(--white)"/>
        <circle cx="204" cy="466" r="23" fill="var(--white)" stroke="var(--ink)" stroke-width="1"/>
      </g>
    </svg>
    <div class="wordmark"><span>veltrix</span><span class="wordmark-dot"></span></div>
    <div class="wordmark cd-wordmark"><span>veltrix</span><span class="wordmark-dot"></span></div>
    <div class="letter-footer contact">
      <p>C-14 Block no-d Lahore Pakistan</p>
      <p>Ph:0921112233 -345556677-778899</p>
      <p>email: nadia_vpg@mailbox.com</p>
      <p>web: www.veltrixpg.com</p>
    </div>
  </section>

  <section class="card-front" aria-label="Business card front">
    <div class="wordmark"><span>veltrix</span><span class="wordmark-dot"></span></div>
    <div class="name-tab">
      <p class="person-name">Tariq Mansoor</p>
      <p class="person-role">Manager</p>
    </div>
    <div class="card-contact contact">
      <p>C-14 Block no-d Lahore Pakistan</p>
      <p>Ph:0921112233 -345556677-778899</p>
      <p>email: nadia_vpg@mailbox.com</p>
      <p>web: www.veltrixpg.com</p>
    </div>
  </section>

  <section class="card-back" aria-label="Business card back">
    <p class="tagline">Prime Solution Partners</p>
    <p class="url">www.primesp.com.pk</p>
  </section>

</main>
</body>
</html>
```